Can you make a cool and versatile Talvern Ridge Powerpoint template?
See www.talvernridge.co.uk and http://www.linkedin.com/company/talvern-ridge-ltd/ (on the right) to see how the logos are currently used - with interchangeably white and black backgrounds.
Target Market(s)
Marketing managers, product managers in HR technology, HR consultants
Industry/Entity Type
It Company
Font styles to use
Sans Serif
Requirements
Must have
- Master slide design, fonts, color theme, etc. Ideally two variations - one with white background (using colorful logo), one with a darker background (using black/white logo).

```html
<!DOCTYPE html>
<html lang="en">
<head>
<meta charset="utf-8">
<title>Talvern Ridge – Presentation Template</title>
<link rel="stylesheet" href="https://fonts.googleapis.com/css2?family=Fira+Sans:wght@400&family=Open+Sans:wght@800&family=Roboto:wght@700&display=swap">
<style>
  :root {
    --navy-deep: #0b1a4a;
    --navy: #14296a;
    --ring: #1a3377;
    --ring-light: #1f3a82;
    --white: #ffffff;
    --ink: #1c1c1c;
    --tab-dark: #13328f;
    --tab-light: #0a9ed6;
    --tab-active-dark: #ff6a00;
    --tab-active-light: #ffc20e;
    --tab-active-ink: #1a1a1a;
  }
  * { margin: 0; padding: 0; box-sizing: border-box; }
  html, body { width: 1200px; height: 900px; overflow: hidden; background: var(--navy-deep); }
  .slide { position: relative; width: 1200px; height: 900px; overflow: hidden; background: var(--navy-deep); }
  .backdrop { position: absolute; inset: 0; }
  .slide-title {
    position: absolute; left: 195px; top: 100px;
    font-family: "Open Sans", sans-serif; font-weight: 800; font-size: 44px;
    color: var(--white); letter-spacing: 0.5px;
    text-shadow: 2px 3px 4px rgba(0,0,0,0.45);
  }
  .topic-nav { position: absolute; left: 70px; top: 250px; list-style: none; }
  .topic-tab {
    width: 190px; height: 62px; margin-bottom: 19.5px;
    border-radius: 4px;
    background: linear-gradient(160deg, var(--tab-light) 0%, var(--tab-dark) 55%);
    font-family: "Open Sans", sans-serif; font-weight: 800; font-size: 24px;
    color: var(--white); line-height: 62px; padding-left: 19px;
  }
  .topic-tab.is-active {
    background: linear-gradient(160deg, var(--tab-active-light) 0%, var(--tab-active-dark) 60%);
    color: var(--tab-active-ink);
  }
  .content-panel { position: absolute; inset: 0; pointer-events: none; }
  .content-text {
    position: absolute; left: 363px; top: 332px;
    font-family: "Fira Sans", sans-serif; font-weight: 400; font-size: 22px;
    line-height: 40px; color: var(--ink);
  }
  .brand {
    position: absolute; right: 92px; bottom: 33px;
    display: flex; align-items: center; gap: 14px;
    font-family: "Roboto", sans-serif; font-weight: 700; font-size: 28px;
    color: var(--white); letter-spacing: 0.3px;
  }
  .brand-dot { width: 20px; height: 20px; border-radius: 50%; background: var(--white); }
</style>
</head>
<body>
<main class="slide">
  <svg class="backdrop" width="1200" height="900" viewBox="0 0 1200 900" aria-hidden="true">
    <defs>
      <radialGradient id="glow" cx="50%" cy="40%" r="70%">
        <stop offset="0" stop-color="#1d3a8a"/>
        <stop offset="1" stop-color="#0b1a4a"/>
      </radialGradient>
    </defs>
    <rect width="1200" height="900" fill="url(#glow)"/>
    <circle cx="640" cy="640" r="760" fill="none" stroke="var(--ring)" stroke-width="60" opacity="0.6"/>
    <circle cx="640" cy="640" r="560" fill="none" stroke="var(--ring-light)" stroke-width="90" opacity="0.55"/>
    <circle cx="640" cy="640" r="390" fill="none" stroke="var(--ring)" stroke-width="70" opacity="0.6"/>
  </svg>

  <h1 class="slide-title">PRESENTATION TITLE</h1>

  <ul class="topic-nav">
    <li class="topic-tab">TOPIC</li>
    <li class="topic-tab">TOPIC</li>
    <li class="topic-tab">TOPIC</li>
    <li class="topic-tab is-active">TOPIC</li>
    <li class="topic-tab">TOPIC</li>
    <li class="topic-tab">TOPIC</li>
  </ul>

  <svg class="content-panel" width="1200" height="900" viewBox="0 0 1200 900" aria-hidden="true">
    <polygon points="201,192 1110,195 1110,727 270,767" fill="var(--white)"/>
  </svg>

  <div class="content-text">
    <p>Need data visuals/infographics for the following facts:</p>
    <p>Patients</p>
    <p>Prevention is broadly overlooked today</p>
    <p>One-third of Americans who have diabetes don't know it</p>
    <p>50% of men and 64% of women who died suddenly of a heart</p>
    <p>attack, never knew they had cardiovascular disease</p>
    <p>66.3% of Americans are overweight</p>
  </div>

  <div class="brand">
    <span class="brand-dot"></span>
    <span class="brand-name">TALVERN RIDGE</span>
  </div>
</main>
</body>
</html>
```